Website redesign for a technology and engineering company

We'd like to redesign our website which can be found on quorvane.co.nz
!! Please find the designers brief as an uploaded file with all details in there!!
The main purpose for redesign is:
>change of services offered
>old website not very user friendly to maintain or update
Key requirements:
>visually appealing
>easy to navigate
>simple and easy to read
>responsive
>mobile device compatibility
>integrating best SEO practice
All the details are in the attached designer brief document.

```html
<!DOCTYPE html>
<html lang="en">
<head>
<meta charset="utf-8">
<title>Quorvane — Field Operations</title>
<link href="https://fonts.googleapis.com/css2?family=Montserrat:wght@400;500;600;700&display=swap" rel="stylesheet">
<style>
:root{
  --ink:#111214;
  --black:#050505;
  --white:#ffffff;
  --grey-bg:#f3f3f4;
  --muted:#5b5f66;
  --line:#cfd2d8;
  --blue:#3d6bf5;
  --blue-dark:#2f59d9;
  --sky-top:#1d3f77;
  --sky-mid:#4a6e9c;
  --ground:#5a4a3e;
}
*{box-sizing:border-box;margin:0;padding:0}
html,body{width:1200px;height:4326px;overflow:hidden}
body{position:relative;font-family:"Montserrat",sans-serif;color:var(--ink);background:var(--white)}
.abs{position:absolute}
a{color:inherit;text-decoration:none}

/* top bar & header */
.topbar{left:695px;top:0;width:362px;height:34px;background:var(--black);color:#fff;font-size:12px;display:flex;align-items:center}
.topbar .phone{flex:1;padding-left:30px;display:flex;gap:8px;align-items:center}
.topbar .phone b{font-weight:600}
.topbar .touch{background:var(--blue);height:34px;width:108px;display:flex;align-items:center;padding-left:14px;font-size:12px}
.topbar .touch-arrow{background:var(--blue-dark);width:40px;height:34px;display:flex;align-items:center;justify-content:center}
.header{left:0;top:34px;width:1200px;height:45px;background:#fff}
.nav{right:142px;top:48px;display:flex;gap:30px;font-size:12.5px;font-weight:500;letter-spacing:.6px}
.logo-tab{left:148px;top:0;width:176px;height:100px;background:#fff;border-radius:0 0 22px 22px;display:flex;align-items:center;justify-content:center;gap:8px;z-index:3}
.brand{font-weight:600;font-size:28px;color:var(--ink);letter-spacing:.3px}
.brand-dot{width:14px;height:14px;border-radius:50%;background:var(--ink)}

/* hero */
.hero{left:0;top:79px;width:1200px;height:639px;background:linear-gradient(180deg,var(--sky-top) 0%,var(--sky-mid) 62%,#8a94a0 78%,var(--ground) 100%)}
.hero-drone{left:560px;top:70px;width:520px;height:430px;border-radius:40px;background:radial-gradient(ellipse at 50% 45%,rgba(236,238,242,.9) 0%,rgba(200,205,214,.6) 45%,rgba(60,90,140,0) 72%)}
.hero-title{left:143px;top:255px;font-size:64px;line-height:72px;font-weight:700;color:#fff}
.btn-learn{left:144px;top:435px;width:176px;height:47px;display:flex;border:1px solid rgba(255,255,255,.7)}
.btn-learn span{flex:1;display:flex;align-items:center;padding-left:18px;color:#fff;font-size:14px;letter-spacing:.6px}
.btn-learn i{width:47px;background:#fff;display:flex;align-items:center;justify-content:center}
.slide-index{left:58px;top:264px;color:#fff;font-size:11px;width:20px;text-align:center}
.slide-line{left:66px;top:290px;width:1px;height:178px;background:rgba(255,255,255,.6)}
.slide-tab{left:0;top:654px;width:240px;height:64px;background:#fff;display:flex;align-items:center;padding-left:148px;gap:7px}
.slide-tab span{width:6px;height:6px;border-radius:50%;background:#ccc}
.slide-tab span.on{background:#fff;border:1.5px solid #222;width:9px;height:9px}

/* section labels */
.label{font-size:12px;letter-spacing:3px;font-weight:500;display:flex;align-items:center;gap:12px}
.label::after{content:"";width:60px;height:1px;background:currentColor;opacity:.4}
.h-xl{font-size:64px;line-height:72px;font-weight:600}

/* about */
.about-text{left:551px;top:787px;width:510px;font-size:15.5px;line-height:25.5px;color:#333}
.about-photo{left:153px;top:965px;width:896px;height:463px;background:linear-gradient(180deg,#2f67c9 0%,#6b9bd8 35%,#5e6f52 55%,#8a8a84 100%)}
.about-shadow{left:190px;top:1428px;width:850px;height:40px;background:linear-gradient(180deg,rgba(0,0,0,.08),rgba(0,0,0,0))}
.badge{left:861px;top:906px;width:120px;height:120px;border-radius:50%;background:var(--black);display:flex;align-items:center;justify-content:center}
.badge-inner{width:48px;height:48px;border-radius:50%;background:#fff;display:flex;align-items:center;justify-content:center}
.exp{left:153px;top:1359px;width:199px;height:76px;background:#fff;display:flex;align-items:center;gap:8px;padding-left:24px}
.exp b{font-size:36px;font-weight:600}
.exp small{font-size:12.5px;line-height:14px;letter-spacing:.6px;color:#333}

/* services */
.services{left:0;top:1519px;width:1200px;height:637px;background:var(--black)}
.services .label{color:#fff}
.svc{color:#fff}
.svc h3{font-size:24px;line-height:33px;font-weight:600;margin:22px 0 12px}
.svc ul{list-style:none;font-size:14px;color:#ddd}
.svc li{display:flex;gap:10px;align-items:flex-start;margin-bottom:9px;line-height:18px}
.svc li svg{flex:none;margin-top:2px}
.svc-center{left:398px;top:1715px;width:401px;height:490px;background:var(--black)}
.svc-center-photo{left:398px;top:1715px;width:401px;height:440px;background:linear-gradient(180deg,#7d8f7a 0%,#4b5e3c 40%,#2a2f2c 80%,#1a1a1a 100%)}

/* projects */
.projects{left:0;top:2156px;width:1200px;height:840px;background:var(--grey-bg)}
.btn-view{left:876px;top:2346px;width:176px;height:49px;display:flex;border:1px solid var(--blue)}
.btn-view span{flex:1;display:flex;align-items:center;justify-content:center;color:var(--blue);font-size:14px;letter-spacing:.8px}
.btn-view i{width:49px;background:var(--blue);display:flex;align-items:center;justify-content:center}
.shot{position:absolute}
.landscape{left:0;top:2960px;width:1200px;height:367px;background:linear-gradient(180deg,#eef0f2 0%,#b3bac2 18%,#5f6b75 42%,#8f8458 70%,#6c5b3a 100%)}

/* contact */
.contact-item{display:flex;gap:14px;align-items:center}
.contact-item .ico{width:36px;height:36px;border-radius:50%;background:var(--black);display:flex;align-items:center;justify-content:center}
.contact-item small{display:block;font-size:11px;color:#888;margin-bottom:2px}
.contact-item b{font-size:21px;font-weight:500;letter-spacing:.4px}
.form-title{left:670px;top:3432px;font-size:27px;font-weight:500}
.field{left:670px;width:386px;border-bottom:1px solid var(--line);font-size:12px;color:#444}
.field sup{color:#bbb}
.btn-send{left:670px;top:3770px;width:386px;height:54px;background:var(--blue);display:flex;color:#fff}
.btn-send span{flex:1;display:flex;align-items:center;justify-content:center;font-size:16px;letter-spacing:.8px}
.btn-send i{width:56px;border-left:1px solid rgba(255,255,255,.35);display:flex;align-items:center;justify-content:center}

/* footer */
.footer{left:0;top:3905px;width:1200px;height:421px;background:linear-gradient(90deg,#121212 0%,#1b1b1b 55%,#0e0e0e 100%);color:#c9c9c9}
.footer .brand{color:#fff}
.foot-text{font-size:13.5px;line-height:24px;color:#bdbdbd}
.foot-head{font-size:12px;font-weight:600;letter-spacing:1px;color:#fff}
.sub-input{left:790px;top:4029px;width:266px;height:44px;border:1px solid #888;font-size:12.5px;color:#aaa;display:flex;align-items:center;padding-left:16px}
.sub-btn{left:790px;top:4088px;width:266px;height:45px;background:var(--blue);display:flex;color:#fff}
.sub-btn span{flex:1;display:flex;align-items:center;justify-content:center;font-size:14px}
.sub-btn i{width:50px;border-left:1px solid rgba(255,255,255,.35);display:flex;align-items:center;justify-content:center}
.social{left:478px;top:4206px;width:28px;height:28px;border-radius:50%;background:#3a3a3a}
</style>
</head>
<body>

<!-- header -->
<div class="abs header"></div>
<div class="abs logo-tab"><span class="brand-dot"></span><span class="brand">Quorvane</span></div>
<div class="abs topbar">
  <div class="phone">
    <svg width="12" height="12" viewBox="0 0 24 24"><path fill="#fff" d="M6.6 10.8a15 15 0 0 0 6.6 6.6l2.2-2.2c.3-.3.7-.4 1-.2 1.1.4 2.3.6 3.6.6.6 0 1 .4 1 1V20c0 .6-.4 1-1 1A17 17 0 0 1 3 4c0-.6.4-1 1-1h3.5c.6 0 1 .4 1 1 0 1.3.2 2.5.6 3.6.1.3 0 .7-.2 1z"/></svg>
    Phone: <b>080-555-0142</b>
  </div>
  <div class="touch">Get in touch</div>
  <div class="touch-arrow"><svg width="12" height="12" viewBox="0 0 12 12"><path d="M2 10L10 2M4 2h6v6" stroke="#fff" fill="none" stroke-width="1.3"/></svg></div>
</div>
<nav class="abs nav"><a>HOME</a><a>WHAT WE DO</a><a>ABOUT</a><a>PROJECTS</a><a>CONTACT</a></nav>

<!-- hero -->
<section class="abs hero" role="img" aria-label="Photo of a white survey drone flying above a rocky mountain ridge under a blue sky"></section>
<div class="abs hero-drone" role="img" aria-label="White quadcopter drone with camera gimbal"></div>
<div class="abs slide-index" style="top:264px">01</div>
<div class="abs slide-line"></div>
<div class="abs slide-index" style="top:476px">03</div>
<h1 class="abs hero-title">Aerial<br>Surveys</h1>
<a class="abs btn-learn"><span>Learn More</span><i><svg width="18" height="18" viewBox="0 0 18 18"><path d="M3 15L15 3M6 3h9v9" stroke="#111" fill="none" stroke-width="1.6"/></svg></i></a>
<div class="abs slide-tab"><span></span><span></span><span class="on"></span></div>

<!-- about -->
<div class="abs label" style="left:144px;top:790px;color:#444">ABOUT</div>
<h2 class="abs h-xl" style="left:142px;top:806px">Quorvane</h2>
<p class="abs about-text">We are field operations experts with backgrounds in surveying, geoscience, and technical field work. Our purpose is to solve problems in the field, build robust infrastructure &amp; deliver accurate data to our clients.</p>
<div class="abs about-shadow"></div>
<div class="abs about-photo" role="img" aria-label="Solar powered monitoring station on an alpine ridge overlooking mountains and a fiord"></div>
<div class="abs badge">
  <svg class="abs" style="left:0;top:0" width="120" height="120" viewBox="0 0 120 120">
    <defs><path id="ring" d="M60 60 m-44 0 a44 44 0 1 1 88 0 a44 44 0 1 1 -88 0"/></defs>
    <text font-family="Montserrat,sans-serif" font-size="11" font-weight="600" fill="#fff" letter-spacing="3"><textPath href="#ring">CONTACT US • CONTACT US •</textPath></text>
  </svg>
  <div class="badge-inner"><svg width="22" height="22" viewBox="0 0 22 22"><path d="M4 18L18 4M8 4h10v10" stroke="var(--blue)" fill="none" stroke-width="2"/></svg></div>
</div>
<div class="abs exp"><b>15+</b><small>Years of<br>Experience</small></div>

<!-- services -->
<section class="abs services"></section>
<div class="abs label" style="left:142px;top:1596px;color:#fff">SERVICES</div>
<h2 class="abs h-xl" style="left:142px;top:1613px;color:#fff">What we do</h2>
<div class="abs" style="left:0;top:1740px;width:1200px;height:1px;background:#2a2a2a"></div>

<div class="abs svc" style="left:65px;top:1812px;width:300px">
  <svg width="52" height="30" viewBox="0 0 52 30"><g stroke="#fff" stroke-width="2" fill="none"><path d="M4 5h16M32 5h16M12 5v6M40 5v6M12 11h28"/><circle cx="26" cy="16" r="6"/><path d="M20 22l-6 6M32 22l6 6"/></g></svg>
  <h3>UAV &amp; Survey<br>Services</h3>
  <ul>
    <li><svg width="14" height="14" viewBox="0 0 14 14"><circle cx="7" cy="7" r="6" stroke="#fff" fill="none"/><path d="M4 7l2 2 4-4" stroke="#fff" fill="none"/></svg>Orthophotos</li>
    <li><svg width="14" height="14" viewBox="0 0 14 14"><circle cx="7" cy="7" r="6" stroke="#fff" fill="none"/><path d="M4 7l2 2 4-4" stroke="#fff" fill="none"/></svg>Digital Terrain Models</li>
    <li><svg width="14" height="14" viewBox="0 0 14 14"><circle cx="7" cy="7" r="6" stroke="#fff" fill="none"/><path d="M4 7l2 2 4-4" stroke="#fff" fill="none"/></svg>Pointclouds For AEC</li>
    <li><svg width="14" height="14" viewBox="0 0 14 14"><circle cx="7" cy="7" r="6" stroke="#fff" fill="none"/><path d="M4 7l2 2 4-4" stroke="#fff" fill="none"/></svg>Inspections</li>
    <li><svg width="14" height="14" viewBox="0 0 14 14"><circle cx="7" cy="7" r="6" stroke="#fff" fill="none"/><path d="M4 7l2 2 4-4" stroke="#fff" fill="none"/></svg>Volumetrics</li>
  </ul>
  <svg style="margin-top:12px" width="18" height="18" viewBox="0 0 18 18"><path d="M3 3l12 12M15 6v9H6" stroke="#fff" fill="none" stroke-width="1.6"/></svg>
</div>

<div class="abs svc-center"></div>
<div class="abs svc-center-photo" role="img" aria-label="Field technician in hi-vis shirt beside a pole-mounted instrument box in bush"></div>
<div class="abs svc" style="left:463px;top:1852px;width:300px">
  <svg width="34" height="40" viewBox="0 0 34 40"><g stroke="#fff" stroke-width="2" fill="none"><circle cx="12" cy="6" r="4"/><path d="M12 12v14l-6 12M12 26l6 12M4 18h16M26 4v34M22 38l4-12 4 12"/></g></svg>
  <h3>Technical Field<br>Operations</h3>
  <ul>
    <li><svg width="14" height="14" viewBox="0 0 14 14"><circle cx="7" cy="7" r="6" stroke="#fff" fill="none"/><path d="M4 7l2 2 4-4" stroke="#fff" fill="none"/></svg>Install &amp; Maintenance of<br>Remote Infrastructure</li>
    <li><svg width="14" height="14" viewBox="0 0 14 14"><circle cx="7" cy="7" r="6" stroke="#fff" fill="none"/><path d="M4 7l2 2 4-4" stroke="#fff" fill="none"/></svg>Standalone Solar Power<br>Solutions</li>
    <li><svg width="14" height="14" viewBox="0 0 14 14"><circle cx="7" cy="7" r="6" stroke="#fff" fill="none"/><path d="M4 7l2 2 4-4" stroke="#fff" fill="none"/></svg>Monitoring: Environmental<br>&amp; Natural Hazards</li>
  </ul>
  <svg style="margin-top:20px" width="26" height="16" viewBox="0 0 26 16"><path d="M1 8h23M17 1l7 7-7 7" stroke="#fff" fill="none" stroke-width="1.6"/></svg>
</div>

<div class="abs svc" style="left:862px;top:1808px;width:300px">
  <svg width="42" height="38" viewBox="0 0 42 38"><g stroke="#fff" stroke-width="2" fill="none"><circle cx="14" cy="12" r="7"/><circle cx="14" cy="12" r="2.5"/><circle cx="29" cy="26" r="8"/><circle cx="29" cy="26" r="3"/></g></svg>
  <h3>Design &amp;<br>Prototyping</h3>
  <ul>
    <li><svg width="14" height="14" viewBox="0 0 14 14"><circle cx="7" cy="7" r="6" stroke="#fff" fill="none"/><path d="M4 7l2 2 4-4" stroke="#fff" fill="none"/></svg>Design Mechanical Parts</li>
    <li><svg width="14" height="14" viewBox="0 0 14 14"><circle cx="7" cy="7" r="6" stroke="#fff" fill="none"/><path d="M4 7l2 2 4-4" stroke="#fff" fill="none"/></svg>Drawings &amp; Models For<br>Manufacturing</li>
    <li><svg width="14" height="14" viewBox="0 0 14 14"><circle cx="7" cy="7" r="6" stroke="#fff" fill="none"/><path d="M4 7l2 2 4-4" stroke="#fff" fill="none"/></svg>Monitoring Solutions</li>
    <li><svg width="14" height="14" viewBox="0 0 14 14"><circle cx="7" cy="7" r="6" stroke="#fff" fill="none"/><path d="M4 7l2 2 4-4" stroke="#fff" fill="none"/></svg>Prototyping</li>
  </ul>
  <svg style="margin-top:12px" width="18" height="18" viewBox="0 0 18 18"><path d="M3 3l12 12M15 6v9H6" stroke="#fff" fill="none" stroke-width="1.6"/></svg>
</div>

<!-- projects -->
<section class="abs projects"></section>
<div class="abs label" style="left:144px;top:2280px;color:#444">PROJECTS</div>
<h2 class="abs h-xl" style="left:142px;top:2298px">Project Cases</h2>
<p class="abs" style="left:144px;top:2378px;font-size:15.5px;letter-spacing:.4px;color:#333">Check out some projects we have been working on</p>
<a class="abs btn-view"><span>View All</span><i><svg width="18" height="18" viewBox="0 0 18 18"><path d="M3 15L15 3M6 3h9v9" stroke="#fff" fill="none" stroke-width="1.6"/></svg></i></a>

<div class="shot" style="left:146px;top:2487px;width:215px;height:236px;background:linear-gradient(180deg,#3d78c9,#4c7a3a 60%,#8a8f95)" role="img" aria-label="Technician installing a satellite dish on a hut roof"></div>
<div class="shot" style="left:379px;top:2441px;width:366px;height:282px;background:linear-gradient(180deg,#c6cbd1 0%,#8b949c 45%,#5c8c3e 70%,#4c7a32 100%)" role="img" aria-label="Survey instruments and a utility vehicle on a grassy hilltop"></div>
<div class="shot" style="left:763px;top:2473px;width:138px;height:125px;background:linear-gradient(180deg,#8fb2d6,#4d6e8a 55%,#b23a2f 80%,#222)" role="img" aria-label="Inflatable boat on open water near rocky islands"></div>
<div class="shot" style="left:921px;top:2473px;width:134px;height:125px;background:linear-gradient(180deg,#c7d6ea,#a3b4c8 70%,#e3e8ee)" role="img" aria-label="Monitoring mast in snow"></div>
<div class="shot" style="left:763px;top:2616px;width:292px;height:267px;background:linear-gradient(180deg,#3a6fc4 0%,#6d93c8 35%,#5e6b52 60%,#8a8a84 100%)" role="img" aria-label="Solar monitoring station on an alpine ridge"></div>
<div class="shot" style="left:220px;top:2742px;width:216px;height:179px;background:linear-gradient(135deg,#c4b49a,#9d8d74)" role="img" aria-label="Grey instrument enclosure on a wooden bench"></div>
<div class="shot" style="left:455px;top:2742px;width:290px;height:196px;background:linear-gradient(90deg,#5d6a4c,#9aa39a 50%,#6b6f5e)" role="img" aria-label="Aerial view of a river channel and bridge"></div>

<div class="abs landscape" role="img" aria-label="Panorama of a hilltop station overlooking a river valley and distant mountains"></div>

<!-- contact -->
<div class="abs label" style="left:144px;top:3407px;color:#444">CONTACT US</div>
<h2 class="abs h-xl" style="left:142px;top:3422px;line-height:62px">Get in touch<br>with us!</h2>
<div class="abs contact-item" style="left:146px;top:3588px">
  <span class="ico"><svg width="16" height="16" viewBox="0 0 24 24"><path fill="#fff" d="M6.6 10.8a15 15 0 0 0 6.6 6.6l2.2-2.2c.3-.3.7-.4 1-.2 1.1.4 2.3.6 3.6.6.6 0 1 .4 1 1V20c0 .6-.4 1-1 1A17 17 0 0 1 3 4c0-.6.4-1 1-1h3.5c.6 0 1 .4 1 1 0 1.3.2 2.5.6 3.6.1.3 0 .7-.2 1z"/></svg></span>
  <div><small>Call Us:</small><b>080-555-0142</b></div>
</div>
<div class="abs contact-item" style="left:146px;top:3660px">
  <span class="ico"><svg width="16" height="14" viewBox="0 0 16 14"><rect x="1" y="2" width="14" height="10" rx="1" fill="#fff"/><path d="M1 3l7 5 7-5" stroke="#111" fill="none" stroke-width="1.3"/></svg></span>
  <div><small>Email us:</small><b>hi@quorvane.nz</b></div>
</div>

<h3 class="abs form-title">Send Us a Message</h3>
<div class="abs field" style="top:3492px;height:24px">Name<sup>*</sup></div>
<div class="abs field" style="top:3542px;height:23px">Email<sup>*</sup></div>
<div class="abs field" style="top:3592px;height:23px">Subject<sup>*</sup></div>
<div class="abs field" style="top:3643px;height:100px">Mesage (Optional)</div>
<a class="abs btn-send"><span>Send Message</span><i><svg width="18" height="18" viewBox="0 0 18 18"><path d="M3 15L15 3M6 3h9v9" stroke="#fff" fill="none" stroke-width="1.6"/></svg></i></a>

<!-- footer -->
<footer class="abs footer"></footer>
<div class="abs" style="left:150px;top:3972px;display:flex;align-items:center;gap:10px"><span class="brand-dot" style="background:#fff"></span><span class="brand" style="color:#fff;font-size:34px">Quorvane</span></div>
<p class="abs foot-text" style="left:149px;top:4024px;width:380px">We are field operations experts with backgrounds in surveying, geoscience, &amp; technical field work. Our purpose is to solve problems in the field, build robust infrastructure and deliver accurate data to our clients.</p>
<p class="abs" style="left:145px;top:4200px;font-size:12.5px;color:#bbb">© Quorvane 2024. All Rights Reserved.</p>
<p class="abs" style="left:145px;top:4225px;font-size:12.5px;color:#bbb">Privacy Policy &nbsp;<span style="color:#555">|</span>&nbsp; Disclaimer</p>
<div class="abs social"></div>

<div class="abs foot-head" style="left:657px;top:3984px">QUICK LINKS</div>
<div class="abs foot-text" style="left:657px;top:4018px;line-height:29px">About<br>Contact</div>
<div class="abs foot-head" style="left:791px;top:3984px">SUBSCRIBE TO OUR EMAIL</div>
<div class="abs sub-input">Enter your email here..</div>
<a class="abs sub-btn"><span>Subscribe</span><i><svg width="16" height="16" viewBox="0 0 18 18"><path d="M3 15L15 3M6 3h9v9" stroke="#fff" fill="none" stroke-width="1.6"/></svg></i></a>
<p class="abs" style="left:791px;top:4150px;width:270px;font-size:11.5px;line-height:18px;color:#999">By subscribing, you agree with our privacy policy and our terms of service.</p>

</body>
</html>
```